Garden Design Flier

I would like a PDF of this half page A4 flier in soft green tones with dark green leaves.

Target Market(s)

Home owners and real estate agents

Font styles to use
Serif
Other font styles liked:
• Papyrus

Colors
acd136
9bcb3c
cadf82
fefdec

Requirements
Must have
• Green tones
Nice to have
• Leaves, vines, lawns
Should not have
• Open to ideas, but classic style

```html
<!DOCTYPE html>
<html lang="en">
<head>
<meta charset="UTF-8">
<title>Fernleigh Gardens Flier</title>
<link rel="stylesheet" href="https://fonts.googleapis.com/css2?family=League+Spartan:wght@700&family=Didact+Gothic&display=swap">
<style>
  :root {
    --forest: #2d5242;
    --paper: #ffffff;
    --ink: #111111;
    --fern-light: #5f8a4a;
    --fern-dark: #1c3322;
  }
  * { margin: 0; padding: 0; box-sizing: border-box; }
  html, body { width: 848px; height: 1200px; overflow: hidden; background: var(--paper); }
  .flier {
    position: relative;
    width: 848px;
    height: 1200px;
    background: var(--paper);
    font-family: "Didact Gothic", "Helvetica Neue", Arial, sans-serif;
    color: var(--forest);
    text-align: center;
  }
  .hero-foliage {
    position: absolute;
    top: 0; left: 0;
    width: 848px; height: 345px;
    background:
      radial-gradient(ellipse 45% 60% at 38% 45%, #7fa361 0%, rgba(127,163,97,0) 70%),
      radial-gradient(ellipse 35% 50% at 78% 40%, #5c8a4a 0%, rgba(92,138,74,0) 70%),
      linear-gradient(160deg, var(--fern-dark) 0%, #3b6a3c 45%, #29452c 100%);
  }
  .brand-name {
    position: absolute;
    top: 408px; left: 0; width: 100%;
    font-family: "League Spartan", "Helvetica Neue", Arial, sans-serif;
    font-weight: 700;
    font-size: 58px;
    letter-spacing: 0.06em;
    line-height: 1;
  }
  .brand-sub {
    position: absolute;
    top: 508px; left: 0; width: 100%;
    font-family: "League Spartan", "Helvetica Neue", Arial, sans-serif;
    font-weight: 700;
    font-size: 26px;
    letter-spacing: 0.42em;
    padding-left: 0.42em;
    line-height: 1;
  }
  .owner {
    position: absolute;
    top: 552px; left: 0; width: 100%;
    font-size: 19px;
    line-height: 1;
  }
  .services {
    position: absolute;
    top: 588px; left: 134px; width: 580px;
    font-size: 21px;
    line-height: 33.5px;
    color: var(--ink);
  }
  .qualification {
    position: absolute;
    top: 752px; left: 0; width: 100%;
    font-size: 17px;
  }
  .tagline {
    position: absolute;
    top: 884px; left: 0; width: 100%;
    font-size: 44px;
    line-height: 1.2;
  }
  .contact-band {
    position: absolute;
    left: 0; top: 1030px;
    width: 848px; height: 170px;
    background: var(--forest);
    color: var(--paper);
    padding-top: 40px;
    font-size: 16px;
    line-height: 31px;
  }
</style>
</head>
<body>
  <main class="flier">
    <div class="hero-foliage" role="img" aria-label="Close-up photograph of lush green fern fronds"></div>

    <h1 class="brand-name">FERNLEIGH</h1>
    <p class="brand-sub">GARDENS</p>
    <p class="owner">Liam Hartwell</p>

    <p class="services">All your gardening and landscaping needs from design and installation to general maintenance Bespoke vegetable gardens and potager designs created to suite your site and requirements.</p>

    <p class="qualification">Certificate 3. Horticulture. Greenvale College</p>

    <p class="tagline">Design. Install. Grow. Tend. Enjoy</p>

    <footer class="contact-band">
      <p>For more information, kindly email us at liam@fernleighgardens.com.au. You can<br>also call us at 0400-123456.</p>
      <p>ABN: 12345678901</p>
    </footer>
  </main>
</body>
</html>
```